Velbrook Naturals - High Quality Organic Cleaning Product

A product label for a foaming hand soap. Company is called "Velbrook Naturals" and the tagline is "The Cleaner Cleaner". Maybe lighter blue background with red letters, but open to what looks good. Want it to be a simple, clean and sophisticated design that looks fresh and stands out. This product has high quality organic ingredients hence the ingredients are "velbrook naturals" than other toxic chemical cleaners. Attached is label specifications as well as an image for stock language for left and right side of label for reference. Parts can be omitted, added or mixed and matched as needed.
Went on vacation/holiday
Moms

```html
<!DOCTYPE html>
<html lang="en">
<head>
<meta charset="utf-8">
<title>Velbrook Naturals Foaming Hand Soap Label</title>
<link href="https://fonts.googleapis.com/css2?family=Playfair+Display:wght@700;800&family=Poppins:wght@600;700&display=swap" rel="stylesheet">
<style>
  :root {
    --page: #f3f3f6;
    --label-white: #ffffff;
    --lavender-light: #97a1d4;
    --lavender-dark: #5f6a9f;
    --ink: #5b64a8;
    --tagline-red: #d3101f;
    --text-white: #ffffff;
  }
  html, body {
    margin: 0;
    width: 1200px;
    height: 1117px;
    overflow: hidden;
    background: var(--page);
  }
  .label {
    position: absolute;
    left: 280px;
    top: 58px;
    width: 640px;
    height: 1000px;
    background: var(--label-white);
    box-shadow: 0 2px 14px rgba(60, 70, 120, 0.12);
    overflow: hidden;
  }
  .label__panel {
    position: absolute;
    left: 0;
    top: 0;
    width: 640px;
    height: 720px;
  }
  .brand {
    position: absolute;
    left: 0;
    width: 100%;
    text-align: center;
    margin: 0;
  }
  .brand__name {
    top: 140px;
    font-family: "Playfair Display", serif;
    font-weight: 800;
    font-size: 56px;
    letter-spacing: -0.5px;
    color: var(--text-white);
  }
  .brand__tagline {
    top: 232px;
    font-family: "Poppins", sans-serif;
    font-weight: 600;
    font-size: 33px;
    color: var(--tagline-red);
  }
  .product-name {
    position: absolute;
    left: 0;
    top: 440px;
    width: 100%;
    text-align: center;
    font-family: "Playfair Display", serif;
    font-weight: 700;
    color: var(--text-white);
    margin: 0;
    line-height: 0.95;
  }
  .product-name__line--large { display: block; font-size: 86px; }
  .product-name__line--small { display: block; font-size: 78px; }
  .claims {
    position: absolute;
    left: 40px;
    top: 770px;
    width: 560px;
    display: flex;
    justify-content: space-between;
    align-items: flex-start;
  }
  .claim {
    width: 110px;
    display: flex;
    flex-direction: column;
    align-items: center;
  }
  .claim__icon { width: 72px; height: 72px; }
  .claim__text {
    margin-top: 10px;
    font-family: "Poppins", sans-serif;
    font-weight: 700;
    font-size: 13px;
    line-height: 1.2;
    text-align: center;
    color: var(--ink);
    text-transform: uppercase;
  }
  .claims__divider {
    width: 2px;
    height: 88px;
    margin-top: 12px;
    background: var(--ink);
    opacity: 0.8;
  }
  .volume {
    position: absolute;
    left: 0;
    top: 902px;
    width: 100%;
    text-align: center;
    font-family: "Poppins", sans-serif;
    font-weight: 700;
    font-size: 24px;
    color: var(--ink);
    margin: 0;
  }
  .label__stripe {
    position: absolute;
    left: 0;
    top: 960px;
    width: 100%;
    height: 20px;
    background: var(--ink);
    opacity: 0.85;
  }
</style>
</head>
<body>
  <section class="label">
    <svg class="label__panel" viewBox="0 0 640 720" aria-hidden="true">
      <defs>
        <linearGradient id="panelGradient" x1="0" y1="0" x2="1" y2="0">
          <stop offset="0" stop-color="#97a1d4"/>
          <stop offset="0.6" stop-color="#6c77ad"/>
          <stop offset="1" stop-color="#5f6a9f"/>
        </linearGradient>
      </defs>
      <path d="M0 0 H640 V672 Q320 712 0 672 Z" fill="url(#panelGradient)"/>
    </svg>

    <p class="brand brand__name">Velbrook Naturals</p>
    <p class="brand brand__tagline">Simply Fresh Hands</p>

    <h1 class="product-name">
      <span class="product-name__line--large">Foaming</span>
      <span class="product-name__line--small">Hand Soap</span>
    </h1>

    <div class="claims">
      <div class="claim">
        <svg class="claim__icon" viewBox="0 0 72 72" aria-hidden="true">
          <circle cx="36" cy="36" r="33" fill="none" stroke="#5b64a8" stroke-width="3"/>
          <path d="M24 37 L32 45 L49 27" fill="none" stroke="#5b64a8" stroke-width="3.5" stroke-linecap="round" stroke-linejoin="round"/>
        </svg>
        <span class="claim__text">100%<br>Natural</span>
      </div>
      <div class="claims__divider"></div>
      <div class="claim">
        <svg class="claim__icon" viewBox="0 0 72 72" aria-hidden="true">
          <circle cx="36" cy="36" r="33" fill="none" stroke="#5b64a8" stroke-width="3"/>
          <circle cx="36" cy="36" r="26" fill="none" stroke="#5b64a8" stroke-width="2"/>
          <line x1="18" y1="54" x2="54" y2="18" stroke="#5b64a8" stroke-width="3"/>
        </svg>
        <span class="claim__text">Cruelty<br>Free</span>
      </div>
      <div class="claims__divider"></div>
      <div class="claim">
        <svg class="claim__icon" viewBox="0 0 72 72" aria-hidden="true">
          <circle cx="36" cy="36" r="33" fill="none" stroke="#5b64a8" stroke-width="3"/>
          <line x1="13" y1="59" x2="59" y2="13" stroke="#5b64a8" stroke-width="3"/>
        </svg>
        <span class="claim__text">Non<br>GMO</span>
      </div>
      <div class="claims__divider"></div>
      <div class="claim">
        <svg class="claim__icon" viewBox="0 0 72 72" aria-hidden="true">
          <circle cx="36" cy="36" r="33" fill="none" stroke="#5b64a8" stroke-width="3"/>
          <rect x="30" y="18" width="12" height="34" rx="6" fill="none" stroke="#5b64a8" stroke-width="2.5"/>
          <line x1="13" y1="59" x2="59" y2="13" stroke="#5b64a8" stroke-width="3"/>
        </svg>
        <span class="claim__text">Paraben<br>Free</span>
      </div>
    </div>

    <p class="volume">12 OZ (355ML)</p>
    <div class="label__stripe"></div>
  </section>
</body>
</html>
```